Whitmore Business Card Design

The name of the business is Dara Whitmore, CPA LLC
The service that we offer is Accounting, Tax & Consulting Services. I need it to have the following items:
Dara Whitmore, Principal
Phone Number
Email Address
Physical Address

I have attached the company logo, one in black and one in white. Please provide a design in black background and the other in white background. Please include "Accounting, Tax & Consulting Services". I want the business card to be clean and very professional.

```html
<!DOCTYPE html>
<html lang="en">
<head>
<meta charset="UTF-8">
<title>Dara Whitmore, CPA LLC – Business Cards</title>
<link rel="stylesheet" href="https://fonts.googleapis.com/css2?family=Montserrat:wght@400;500;600&family=Oswald:wght@500&family=Open+Sans:wght@400&display=swap">
<style>
  :root {
    --backdrop: #1c1c1e;
    --card-dark: #3a3a3c;
    --card-dark-pattern: #333335;
    --card-light: #ffffff;
    --ink: #3b3b3d;
    --ink-soft: #6e6e72;
    --brand-red: #8e1b1f;
    --faint-grey: #ececec;
    --faint-red: #f6e9ea;
    --white: #ffffff;
  }
  * { box-sizing: border-box; margin: 0; padding: 0; }
  html, body {
    width: 1200px; height: 800px; overflow: hidden;
    background: var(--backdrop);
  }
  .stage {
    width: 1200px; height: 800px;
    display: flex; flex-direction: column; align-items: center; justify-content: center;
    gap: 36px;
  }
  .card {
    width: 560px; height: 320px; position: relative; overflow: hidden;
    box-shadow: 0 6px 18px rgba(0,0,0,.45);
  }

  /* Front – dark */
  .card--front { background: var(--card-dark); }
  .card--front .pattern-field {
    position: absolute; inset: 0;
    background: linear-gradient(135deg, var(--card-dark-pattern), var(--card-dark) 60%, var(--card-dark-pattern));
  }
  .front-brand {
    position: absolute; right: 34px; top: 122px;
    display: flex; align-items: center; gap: 10px;
    font-family: "Montserrat", sans-serif; font-weight: 600; font-size: 15px;
    color: var(--white); letter-spacing: .04em;
  }
  .front-brand .brand-square { width: 14px; height: 14px; background: var(--white); }
  .tagline {
    position: absolute; left: 0; right: 0; bottom: 70px; text-align: center;
    font-family: "Montserrat", sans-serif; font-weight: 600; font-size: 11px;
    letter-spacing: .28em; color: var(--white); text-transform: uppercase;
  }

  /* Back – light */
  .card--back { background: var(--card-light); }
  .card--back .mark-field {
    position: absolute; left: 250px; top: 0; width: 310px; height: 320px;
    background: linear-gradient(160deg, var(--faint-grey) 0%, #f6f6f6 45%, var(--faint-red) 100%);
    opacity: .75;
  }
  .firm {
    position: absolute; left: 40px; top: 70px;
    font-family: "Montserrat", sans-serif;
  }
  .firm-name {
    display: flex; align-items: center; gap: 9px;
    font-weight: 500; font-size: 19px; color: var(--ink); letter-spacing: .01em;
  }
  .firm-name .brand-square { width: 13px; height: 13px; background: var(--ink); }
  .firm-role {
    margin-top: 4px; font-size: 11.5px; letter-spacing: .14em;
    color: var(--ink-soft); text-transform: uppercase;
  }
  .contact {
    position: absolute; left: 60px; bottom: 40px;
    font-family: "Open Sans", sans-serif; font-size: 11.5px; color: var(--ink-soft);
    line-height: 1.5;
  }
  .contact .address { margin-bottom: 8px; }
  .contact-list { list-style: none; }
  .contact-list li { display: flex; align-items: center; gap: 8px; }
  .contact-list svg { width: 10px; height: 10px; fill: var(--brand-red); flex: none; }
  .person {
    position: absolute; right: 40px; top: 150px; text-align: right;
  }
  .person-name {
    font-family: "Oswald", sans-serif; font-weight: 500; font-size: 22px;
    color: var(--brand-red); text-transform: uppercase; letter-spacing: .01em;
  }
  .person-title {
    font-family: "Open Sans", sans-serif; font-size: 11.5px; color: var(--ink-soft);
  }
</style>
</head>
<body>
<main class="stage">

  <section class="card card--front" aria-label="Business card front">
    <div class="pattern-field" role="img" aria-label="Subtle embossed repeating brand pattern in dark grey"></div>
    <div class="front-brand"><span class="brand-square"></span>Dara Whitmore, CPA LLC</div>
    <p class="tagline">Accounting, Tax &amp; Consulting Services</p>
  </section>

  <section class="card card--back" aria-label="Business card back">
    <div class="mark-field" role="img" aria-label="Large faint brand decoration in light grey and pale red"></div>

    <div class="firm">
      <div class="firm-name"><span class="brand-square"></span>Dara Whitmore, CPA LLC</div>
      <div class="firm-role">Certified Public Accountant</div>
    </div>

    <div class="person">
      <div class="person-name">Dara Whitmore</div>
      <div class="person-title">Principal</div>
    </div>

    <div class="contact">
      <p class="address">412 Larkspur Court<br>Juneau, Alaska 99801</p>
      <ul class="contact-list">
        <li>
          <svg viewBox="0 0 10 10" aria-hidden="true"><path d="M2 0.5 L3.6 2.6 L2.8 3.6 Q4 6 6.4 7.2 L7.4 6.4 L9.5 8 L8.4 9.5 Q3.5 9 0.5 1.6 Z"/></svg>
          907-555-0148
        </li>
        <li>
          <svg viewBox="0 0 10 10" aria-hidden="true"><path d="M0 2 H10 V8.5 H0 Z M0.6 2.4 L5 5.6 L9.4 2.4" stroke="#fff" stroke-width=".8"/></svg>
          name@darawhitmorecpa.com
        </li>
        <li>
          <svg viewBox="0 0 10 10" aria-hidden="true"><circle cx="5" cy="5" r="4.6"/><path d="M0.5 5 H9.5 M5 0.5 V9.5" stroke="#fff" stroke-width=".7"/></svg>
          www.darawhitmorecpa.com
        </li>
      </ul>
    </div>
  </section>

</main>
</body>
</html>
```